electrical automation company needs a letterhead design

we need a letter head designed for our new electrical automation company. Our company color are orange and blue as you'll see from our logo attached

Target Market(s)

Domestic, commercial and industrial electrical clients

Industry/Entity Type

Electrical

Contact Information for Business Card

I need to update my business card to make it more eye catching I have attached my old business card designs, logo and new trifold brochure to give you an idea

Font styles to use
Sans Serif

Colors
f37122
0393ce

Requirements
Must have
• harbor electrical logo
my name
phone number
email
website
Nice to have
• QR code linked to my website
list of some services
- domestic
- commercial
- industrial

```html
<!DOCTYPE html>
<html lang="en">
<head>
<meta charset="utf-8">
<title>Harbor Electrical – Letterhead</title>
<link rel="stylesheet" href="https://fonts.googleapis.com/css2?family=Open+Sans:wght@400;600;700&display=swap">
<style>
  :root {
    --blue: #0393ce;
    --blue-deep: #0672b8;
    --orange: #f37122;
    --ink: #2b2b2b;
    --paper: #ffffff;
    --backdrop: #e4e5e6;
  }
  * { margin: 0; padding: 0; box-sizing: border-box; }
  html, body { width: 1200px; height: 945px; overflow: hidden; }
  body {
    background: var(--backdrop);
    font-family: "Open Sans", Arial, sans-serif;
    color: var(--ink);
  }
  .letterhead {
    position: absolute;
    left: 282px;
    top: 22px;
    width: 636px;
    height: 900px;
    background: var(--paper);
    box-shadow: 0 2px 10px rgba(0,0,0,0.12);
    overflow: hidden;
  }
  .brand {
    position: absolute;
    left: 44px;
    top: 48px;
    display: flex;
    align-items: center;
    gap: 10px;
  }
  .brand-dot {
    width: 26px; height: 26px;
    border-radius: 50%;
    background: var(--blue-deep);
  }
  .brand-name {
    font-size: 18px;
    font-weight: 700;
    color: var(--blue-deep);
    line-height: 1;
  }
  .letter-body {
    position: absolute;
    left: 62px;
    top: 168px;
    width: 500px;
  }
  .salutation {
    font-size: 14px;
    font-weight: 700;
    margin-bottom: 14px;
  }
  .letter-body p {
    font-size: 11.2px;
    line-height: 1.42;
    text-align: justify;
    margin: 0 0 16px 28px;
  }
  .signature {
    position: absolute;
    left: 104px;
    top: 555px;
    width: 140px;
    height: 48px;
    background: linear-gradient(90deg, #f1f1f1, #e2e2e2);
    border-radius: 4px;
  }
  .footer-wave {
    position: absolute;
    left: 0;
    bottom: 0;
    width: 636px;
    height: 270px;
  }
  .contact {
    position: absolute;
    left: 34px;
    bottom: 26px;
    color: #fff;
    font-size: 11px;
    line-height: 1.5;
  }
  .contact-name {
    font-weight: 700;
    font-size: 12px;
    letter-spacing: 0.5px;
  }
  .contact-row { display: flex; align-items: center; gap: 14px; }
  .contact-item { display: flex; align-items: center; gap: 6px; }
  .contact-icon { width: 12px; height: 12px; }
  .contact-web b { font-weight: 700; }
</style>
</head>
<body>
  <main class="letterhead">
    <header class="brand">
      <span class="brand-dot"></span>
      <div class="brand-name">Harbor Electrical</div>
    </header>

    <section class="letter-body">
      <h1 class="salutation">Dear Mr. Carter,</h1>
      <p>Lorem Ipsum is simply dummy text of the printing and typesetting industry. Lorem Ipsum has been the industry's standard dummy text ever since the 1500s, when an unknown printer took a galley of type and scrambled it to make a type specimen book. It has survived not only five centuries, but also the leap into electronic typesetting, remaining essentially unchanged.</p>
      <p>The standard chunk of Lorem Ipsum used since the 1500s is reproduced below for those interested. Sections 1.10.32 and 1.10.33 from "de Finibus Bonorum et Malorum" by Corvinus are also reproduced in their exact original form, accompanied by English versions from the 1914 translation by H. Rowland</p>
      <p>Lorem Ipsum is simply dummy text of the printing and typesetting industry. Lorem Ipsum has been the industry's standard dummy text ever since the 1500s, when an unknown printer took a galley of type and scrambled it to make a type specimen book. It has survived not only five centuries, but also the leap into electronic typesetting, remaining essentially unchanged. It was popularised in the</p>
      <p>The standard chunk of Lorem Ipsum used since the 1500s is reproduced below for those interested. Sections 1.10.32 and 1.10.33 from "de Finibus Bonorum et Malorum" by Corvinus are also reproduced in their exact original form, accompanied by English versions from the 1914 translation by H. Rowland</p>
    </section>

    <div class="signature" role="img" aria-label="Handwritten signature"></div>

    <svg class="footer-wave" viewBox="0 0 636 270" preserveAspectRatio="none" aria-hidden="true">
      <path d="M0 190 C180 110 430 170 636 0" fill="none" stroke="var(--blue)" stroke-width="5" transform="translate(0,-10)"/>
      <path d="M0 190 C180 110 430 170 636 0" fill="none" stroke="var(--orange)" stroke-width="7"/>
      <path d="M0 200 C180 120 430 180 636 10 L636 270 L0 270 Z" fill="var(--blue-deep)"/>
    </svg>

    <footer class="contact">
      <div class="contact-name">DAN REEVE</div>
      <div class="contact-row">
        <span class="contact-item">
          <svg class="contact-icon" viewBox="0 0 12 12"><circle cx="6" cy="6" r="6" fill="var(--orange)"/><path d="M4 3.2l1.1 1.5-.6.7c.4.9 1.1 1.6 2 2l.7-.6 1.5 1.1-.5 1c-2.5-.3-4.4-2.2-4.7-4.7z" fill="#fff"/></svg>
          0400 318 725
        </span>
        <span class="contact-item">
          <svg class="contact-icon" viewBox="0 0 12 12"><circle cx="6" cy="6" r="6" fill="var(--orange)"/><rect x="3" y="4" width="6" height="4.2" fill="none" stroke="#fff" stroke-width="0.9"/><path d="M3 4l3 2.4L9 4" fill="none" stroke="#fff" stroke-width="0.9"/></svg>
          dan@harbor-brightgrid.com.au
        </span>
      </div>
      <div class="contact-web">www.<b>harbor-brightgrid</b>.com.au</div>
    </footer>
  </main>
</body>
</html>
```